Sehr angenehme und professionelle Zusammenarbeit!
Zielgruppe
Ich bin ein Consultant, der sich jetzt selbständig macht. Alles weitere steht in meinen Briefing. Dort findet ihr Fotos, mein Logo und damit auch die Farben, die ich mir wünsche. Meine Zielgruppe sind überwiegend Firmen, aber auch deren Mitarbeitende.
Aufgabenstellung
Die Struktur habe ich versucht zu beschreiben und hoffentlich auch alles über mich und mein Business. Ich freue mich auf eure kreativen und individuellen Vorschläge und bemühe mich zeitnah Feedback zu geben. Manchmal kann es den einen oder anderen Tag dauern. Bei Fragen gerne melden. Ich werde die Fragen, die für alle relevant sind auch im allgemeinen Kommentarfeld veröffentlichen.

```html
<!DOCTYPE html>
<html lang="de">
<head>
<meta charset="utf-8">
<title>Jonas Albrecht – Für jeden. Das Richtige.</title>
<link href="https://fonts.googleapis.com/css2?family=Montserrat:wght@300;400;600;700&display=swap" rel="stylesheet">
<style>
:root{
  --bg:#d5e6ea;
  --navy:#27287a;
  --blue:#3f6fcf;
  --mid:#4a7fd0;
  --light:#8fafdc;
  --gray:#ececec;
  --ink:#3d4266;
  --footer:#26256e;
  --white:#ffffff;
}
*{box-sizing:border-box;margin:0;padding:0}
html,body{width:1154px;height:1200px;overflow:hidden;background:var(--bg)}
.canvas{position:relative;width:1154px;height:1200px;background:var(--bg);font-family:'Montserrat',sans-serif}
.page{position:absolute;background:var(--white);overflow:hidden;box-shadow:0 2px 8px rgba(40,70,90,.12)}
.sec{position:absolute;left:0;right:0}
.header{position:absolute;left:0;right:0;top:0;height:42px;background:var(--white);z-index:3}
.nav{position:absolute;top:22px;font-size:3.6px;letter-spacing:.2px;color:var(--blue);text-transform:uppercase;white-space:nowrap}
.nav.is-active{font-weight:700;color:var(--navy)}
.brand{position:absolute;left:50%;top:13px;transform:translateX(-50%);display:flex;flex-direction:column;align-items:center;gap:3px}
.brand .dot{width:8px;height:8px;border-radius:50%;background:var(--navy)}
.brand .name{font-size:5px;font-weight:600;letter-spacing:.7px;color:var(--navy);white-space:nowrap;text-transform:uppercase}
.photo{position:absolute}
.wedge{position:absolute;left:0;top:0;width:100%;height:100%}
.hero-claim{position:absolute;color:var(--white);font-size:8px;line-height:1.15;font-weight:300}
.hero-claim strong{display:block;font-weight:700;letter-spacing:.3px}
.copy{position:absolute;font-size:3.3px;line-height:1.45;color:var(--ink)}
.copy p{margin-bottom:3px}
.copy.on-color{color:var(--white)}
.sec-title{position:absolute;left:0;right:0;text-align:center;font-size:6.5px;line-height:1.3;color:var(--navy);font-weight:300}
.sec-title strong{display:block;font-weight:700;letter-spacing:.2px}
.sec-title.on-color{color:var(--white)}
.sec-title.blue{color:var(--blue)}
.btn{position:absolute;background:var(--white);border:.8px solid var(--navy);color:var(--navy);font-size:3.5px;font-weight:700;padding:3px 6px;white-space:nowrap;text-transform:uppercase;display:flex;align-items:center;gap:3px}
.btn .sq{width:6px;height:6px;background:var(--navy)}
.footer{position:absolute;left:0;right:0;bottom:0;height:19px;background:var(--footer);color:var(--white);font-size:3.4px;display:flex;align-items:center;justify-content:space-between;padding:0 30px}
.footer .links{display:flex;gap:12px;text-transform:uppercase}
.label{position:absolute;font-size:4px;font-weight:700;color:var(--navy);text-transform:uppercase;letter-spacing:.2px}
.offer{position:absolute;width:95px;height:27px;color:var(--white);font-size:3.3px;line-height:1.3;padding:4px 0 0 20px;text-transform:uppercase;clip-path:polygon(0 0,100% 0,100% 82%,50% 100%,0 82%)}
.offer strong{display:block;font-weight:700}
.offer.light{background:var(--light)}
.offer.navy{background:var(--navy)}
.offer.deep{background:#2a4aa5}
.offer.bright{background:var(--mid)}
.col{position:absolute;width:64px;text-align:center;font-size:3.2px;line-height:1.45;color:var(--ink)}
.col h4{font-size:3.5px;color:var(--blue);font-weight:700;text-transform:uppercase;margin-bottom:3px}
.eyebrow{position:absolute;left:0;right:0;text-align:center;font-size:4.2px;font-weight:700;color:var(--blue);letter-spacing:.2px;text-transform:uppercase}
.fact{position:absolute;display:flex;gap:4px;width:72px}
.fact svg{flex:0 0 11px;height:11px}
.fact p{font-size:3.1px;line-height:1.4;color:var(--ink)}
.step{position:absolute;left:77px;display:flex;align-items:flex-start;gap:12px}
.step .num{width:19px;height:19px;color:var(--white);font-size:5px;font-weight:600;display:flex;align-items:center;justify-content:center}
.step .txt{font-size:4px;line-height:1.2;color:var(--blue);text-transform:uppercase;padding-top:2px}
.step .txt strong{display:block;font-weight:700}
.num.light{background:var(--light)}
.num.navy{background:var(--navy)}
.num.mid{background:var(--mid)}
.submenu{position:absolute;left:46px;top:36px;width:58px;background:var(--white);z-index:4;padding:1px 0 2px 10px;font-size:3.1px;line-height:2.3;color:var(--ink);text-transform:uppercase}
.submenu .is-active{font-weight:700;color:var(--navy)}
</style>
</head>
<body>
<div class="canvas">

  <section class="page page-home" style="left:46px;top:221px;width:286px;height:931px">
    <header class="header">
      <span class="nav" style="left:30px">Start</span>
      <span class="nav" style="left:65px">Angebote</span>
      <div class="brand"><span class="dot"></span><span class="name">Jonas Albrecht</span></div>
      <span class="nav" style="left:200px">Über mich</span>
      <span class="nav" style="left:239px">Kontakt</span>
    </header>

    <div class="sec" style="top:42px;height:128px">
      <div class="photo" role="img" aria-label="Foto: Berater im Gespräch mit einer Klientin, rosa Lichtschleier" style="inset:0;background:linear-gradient(90deg,#dcd8d5 0%,#b9aaa3 30%,#d8c3cc 50%,#f0a3c7 65%,#ea4f9c 82%,#e3336f 100%)"></div>
      <svg class="wedge" viewBox="0 0 286 128" preserveAspectRatio="none"><polygon points="0,128 0,125 186,97 286,107 286,128" fill="#fff"/></svg>
      <div class="hero-claim" style="right:12px;top:42px;text-align:left"><strong>FÜR JEDEN. DAS RICHTIGE.</strong>Beratung für komplexe<br>Personalsituationen</div>
    </div>

    <div class="copy" style="left:56px;top:171px;width:172px">
      <p>Personalprobleme werden im Tagesgeschäft selten tiefer analysiert und häufig nur kosmetisch behandelt. Die Folge: die Motivation sinkt und Frustration steigt. Es kommt zu Fehlzeiten, die Produktivität lässt nach, mitunter können Ziele nicht erreicht werden.</p>
      <p>Meine Beratung und Prozessbegleitung schließt hier eine Lücke. Sie bietet nachhaltige Lösungen bei komplexen und dysfunktionalen Personalsituationen, die alle Seiten einbezieht: Mitarbeitende, Führungskraft, Organisation.</p>
    </div>

    <div class="sec" style="top:228px;height:86px;background:var(--light)">
      <div class="sec-title on-color" style="top:14px"><strong>IHR NUTZEN</strong>Von Lose zu Win für alle Seiten</div>
      <div class="copy on-color" style="left:56px;top:40px;width:172px">
        <p>Die Ursachen für personelle Probleme sind multifaktoriell und langwierig, die negative Wirkung strahlt auf den/die Mitarbeitende, die Führungskraft, das Team und die Abteilung aus.</p>
        <p>Für jeden. Das Richtige. Bedeutet, dass wir die bestmögliche Lösung erarbeiten, in die alle Sichtweisen einfließen, Wahrnehmungen beachtet werden und eine dysfunktionale Situation nachhaltig aufgelöst wird. So können Entwicklungschancen entstehen.</p>
      </div>
    </div>

    <div class="sec" style="top:314px;height:134px">
      <span class="label" style="left:42px;top:56px">Mitarbeitende/r</span>
      <span class="label" style="left:198px;top:56px">Führungskraft</span>
      <svg style="position:absolute;left:113px;top:28px" width="60" height="60" viewBox="0 0 60 60" aria-hidden="true"><circle cx="30" cy="30" r="28" fill="#3f6fcf"/></svg>
      <span class="label" style="left:0;right:0;text-align:center;top:111px">Organisation</span>
    </div>

    <div class="sec" style="top:448px;height:99px;background:var(--gray)">
      <div class="photo" role="img" aria-label="Foto: Berater im hellblauen Hemd, lächelnd" style="left:42px;top:13px;width:101px;height:73px;background:linear-gradient(135deg,#e7ebef,#9fb6d3 60%,#6d86ad)"></div>
      <div class="photo" role="img" aria-label="Foto: Händedruck zweier Männer im Flur" style="left:144px;top:13px;width:101px;height:73px;background:linear-gradient(90deg,#d7dbe2,#8d9ab8 45%,#efeff2 75%,#c7ccd6)"></div>
      <span class="btn" style="left:106px;top:42px">Zum Kennenlerngespräch</span>
    </div>

    <div class="sec" style="top:547px;height:140px">
      <div class="sec-title" style="top:23px;font-size:6.8px"><strong>MEINE ANGEBOTE</strong>Von der Analyse über Beratung bis zur<br>Wissensvermittlung</div>
      <div class="offer light" style="left:42px;top:61px"><strong>Prozessberatung<br>und -begleitung</strong>Ganzheitlich vom Problem zur Lösung</div>
      <div class="offer navy" style="left:150px;top:61px"><strong>Situationsanalyse</strong>Ein Anfang, mehr Klarheit</div>
      <div class="offer deep" style="left:42px;top:93px"><strong>Persönliches<br>Energie-Coaching</strong>Mit Kraft neue Wege gehen</div>
      <div class="offer bright" style="left:150px;top:93px"><strong>Keynote Speeches &amp; Vorträge</strong>Impulse für neue Denkweisen</div>
    </div>

    <div class="sec" style="top:687px;height:120px;background:var(--gray)">
      <div class="sec-title blue" style="top:20px;font-size:6.8px"><strong>ICH BIN JONAS ALBRECHT</strong>und mein Anspruch ist: Für jeden. Das Richtige.</div>
      <div class="col" style="left:40px;top:56px"><h4>Meine Motivation</h4>Ich möchte Menschen unterstützen, sich aus dysfunktionalen Arbeitssituationen zu lösen, ihr Potenzial zu erkennen und auszuleben. Dafür setze ich mich als selbstständiger Berater ein.</div>
      <div class="col" style="left:111px;top:56px"><h4>Meine Überzeugung</h4>Weil es immer eine bessere Lösung gibt, strebe ich Win-Win-Win-Lösungen an. Und das unbeirrlich gerne. Für den Menschen und fürs Unternehmen, menschlich und wirtschaftlich.</div>
      <div class="col" style="left:182px;top:56px"><h4>Meine Haltung</h4>Ein Personalvorstand sagte mal ganz lakonisch im fränkischen Dialekt: „Am Ende geht's darum, sauba mit die Leut' umgehn.“ Dem habe ich nichts hinzuzufügen.</div>
    </div>

    <div class="sec" style="top:807px;height:105px">
      <div class="photo" role="img" aria-label="Foto: Berater im grauen Pullover" style="left:42px;top:17px;width:101px;height:74px;background:linear-gradient(135deg,#f1f1f1,#b9b9bd 55%,#7d7f88)"></div>
      <div class="photo" role="img" aria-label="Foto: Porträt des Beraters in Nahaufnahme" style="left:144px;top:17px;width:101px;height:74px;background:linear-gradient(90deg,#e9e9ea,#d8c2b0 45%,#b99d88 70%,#e4e4e6)"></div>
      <span class="btn" style="left:106px;top:55px">Mehr über mich</span>
    </div>

    <footer class="footer"><span>© Jonas Albrecht 2022</span><span class="links"><span>Impressum</span><span>Datenschutz</span></span></footer>
  </section>

  <section class="page page-desktop" style="left:391px;top:69px;width:370px;height:209px">
    <header class="header" style="height:54px">
      <span class="nav" style="left:38px;top:27px;font-size:4.6px">Start</span>
      <span class="nav" style="left:84px;top:27px;font-size:4.6px">Angebote</span>
      <div class="brand" style="top:16px"><span class="dot" style="width:10px;height:10px"></span><span class="name" style="font-size:6.4px">Jonas Albrecht</span></div>
      <span class="nav" style="left:259px;top:27px;font-size:4.6px">Über mich</span>
      <span class="nav" style="left:308px;top:27px;font-size:4.6px">Kontakt</span>
    </header>
    <div class="sec" style="top:54px;height:155px">
      <div class="photo" role="img" aria-label="Foto: Berater im Gespräch mit einer Klientin, rosa Lichtschleier" style="inset:0;background:linear-gradient(90deg,#dcd8d5 0%,#b9aaa3 32%,#d8c3cc 52%,#f0a3c7 66%,#ea4f9c 82%,#e3336f 100%)"></div>
      <svg class="wedge" viewBox="0 0 370 155" preserveAspectRatio="none"><polygon points="0,155 0,137 185,117 370,131 370,155" fill="#fff"/></svg>
      <div class="hero-claim" style="right:39px;top:52px;font-size:10.5px;text-align:right"><strong>FÜR JEDEN. DAS RICHTIGE.</strong>Beratung für komplexe<br>Personalsituationen</div>
    </div>
  </section>

  <section class="page page-about" style="left:435px;top:419px;width:286px;height:733px">
    <header class="header">
      <span class="nav" style="left:30px">Start</span>
      <span class="nav" style="left:65px">Angebote</span>
      <div class="brand"><span class="dot"></span><span class="name">Jonas Albrecht</span></div>
      <span class="nav is-active" style="left:200px">Über mich</span>
      <span class="nav" style="left:239px">Kontakt</span>
    </header>

    <div class="sec" style="top:42px;height:194px">
      <div class="photo" role="img" aria-label="Porträtfoto: lächelnder Berater mit Brille im Sakko" style="inset:0;background:linear-gradient(90deg,#f5f5f5 0%,#ecebe9 50%,#d6c4b6 68%,#b69e8c 78%,#3c4764 100%)"></div>
      <svg class="wedge" viewBox="0 0 286 194" preserveAspectRatio="none"><polygon points="0,127 125,103 286,112 286,194 0,194" fill="#8fafdc"/></svg>
      <div class="hero-claim" style="left:30px;top:37px;color:var(--navy);font-size:7.6px"><strong>FÜR JEDEN. DAS RICHTIGE.</strong>Wie mein Anspruch zur<br>Berufung wurde</div>
      <div class="copy on-color" style="left:56px;top:126px;width:172px">
        <p>„Jonas, du kannst es nicht immer allen recht machen.“ Diesen Satz habe ich häufig gehört. Im Laufe meiner langjährigen Karriere im Personalbereich mit Leitungsfunktion und ebenso in meinem Privatleben. Auch wenn der Satz stimmt, versuche ich immer wieder aufs Neue, Lösungen zu finden, die für alle Beteiligten gut sind.</p>
        <p>Ich selbst kenne aus meinen 20 Jahren als Team- und Abteilungsleiter Phasen, in denen ich Konflikte und Spannungen im Team nicht komplett auflösen konnte. Ich erlebte, wie mein Team nicht das Potenzial ausschöpfen konnte, das jedoch in ihm steckte. Auf der anderen Seite kennen wir harmonische, gut funktionierende Teams, in denen Kommunikation auf Augenhöhe sowie Arbeit und Entwicklung im Vertrauen möglich sind.</p>
      </div>
    </div>

    <div class="sec" style="top:236px;height:147px">
      <div class="eyebrow" style="top:16px">Bankbetriebswirt &nbsp;|&nbsp; Psychologe &nbsp;|&nbsp; Berater</div>
      <svg style="position:absolute;left:0;top:0" width="286" height="147" viewBox="0 0 286 147" font-family="Montserrat, sans-serif">
        <polyline points="54,64 99,87 142,64 186,87 230,64" fill="none" stroke="#3f6fcf" stroke-width="3"/>
        <g fill="#3f6fcf">
          <circle cx="54" cy="64" r="14"/><circle cx="99" cy="87" r="14"/><circle cx="142" cy="64" r="14"/><circle cx="186" cy="87" r="14"/><circle cx="230" cy="64" r="14"/>
        </g>
        <g fill="#fff" font-size="4" font-weight="700" text-anchor="middle">
          <text x="54" y="65.5">1998</text><text x="99" y="88.5">2000</text><text x="142" y="65.5">2017</text><text x="186" y="88.5">2019</text><text x="230" y="65.5">2022</text>
        </g>
        <g fill="#3d4266" font-size="3.2" text-anchor="middle">
          <text x="54" y="37">Ausbildungsleiter</text><text x="54" y="41">und Ausbildung</text><text x="54" y="45">zum Bankkaufmann</text>
          <text x="142" y="41">Personalleiter</text><text x="142" y="45">Sozialwerk Nordstadt</text>
          <text x="230" y="45">Berater</text>
          <text x="99" y="110">Leiter Organisations- und</text><text x="99" y="114">Personalentwicklung,</text><text x="99" y="118">Leiter Personalbetreuung,</text><text x="99" y="122">Change Management,</text><text x="99" y="126">Ausbildungsleiter Regionalbank</text>
          <text x="186" y="110">Personalleiter</text><text x="186" y="114">Mainfeld AG</text>
        </g>
      </svg>
    </div>

    <div class="sec" style="top:383px;height:99px;background:var(--gray)">
      <div class="photo" role="img" aria-label="Foto: Berater vor einer Kirche in der Altstadt" style="left:41px;top:12px;width:67px;height:74px;background:linear-gradient(160deg,#c9b08f,#8e9aa8 55%,#5e6f89)"></div>
      <div class="photo" role="img" aria-label="Foto: Berater auf einer begrünten Straße" style="left:109px;top:12px;width:68px;height:74px;background:linear-gradient(160deg,#8fae7a,#b9c6c9 50%,#6f87ad)"></div>
      <div class="photo" role="img" aria-label="Foto: Schritte auf einem Gehweg" style="left:178px;top:12px;width:66px;height:74px;background:linear-gradient(160deg,#5c6f5a,#9ea39d 50%,#3c4556)"></div>
      <span class="btn" style="left:95px;top:38px">Lassen Sie uns vernetzen <span class="sq"></span><span class="sq"></span></span>
    </div>

    <div class="sec" style="top:482px;height:124px">
      <div class="eyebrow" style="top:18px;color:var(--navy)">Vereinsfan &nbsp;|&nbsp; Festivalgänger &nbsp;|&nbsp; Familienmensch</div>
      <div class="fact" style="left:35px;top:41px"><svg viewBox="0 0 12 12"><circle cx="6" cy="6" r="5" fill="none" stroke="#2a3a90" stroke-width="1.4"/><circle cx="6" cy="6" r="1.8" fill="#2a3a90"/></svg><p>Ich gebe die Hoffnung nie auf. Vereinsfan seit ich denken kann. Mit dem SVN durch Höhen und Tiefen gehen.</p></div>
      <div class="fact" style="left:110px;top:41px"><svg viewBox="0 0 12 12"><path d="M4 2 L11 1 V8.5" fill="none" stroke="#2a3a90" stroke-width="1.3"/><circle cx="3" cy="9.5" r="2" fill="#2a3a90"/><circle cx="9.5" cy="8.5" r="2" fill="#2a3a90"/></svg><p>Für Festivals bin ich nie zu alt. Am liebsten live. Auf der Sommerwiese oder zu Hause im Garten.</p></div>
      <div class="fact" style="left:187px;top:41px"><svg viewBox="0 0 12 12"><polygon points="6,1.5 11.5,11 0.5,11" fill="#2a3a90"/></svg><p>Manchmal muss es extrem sein. Auf einen hohen Gipfel steigen. Die wilden Achterbahnen des Lebens fahren.</p></div>
      <div class="fact" style="left:35px;top:79px"><svg viewBox="0 0 12 12"><g fill="#2a3a90"><circle cx="2.5" cy="4" r="1.5"/><circle cx="6" cy="3.5" r="1.5"/><circle cx="9.5" cy="4" r="1.5"/><rect x="1" y="6" width="3" height="4" rx="1"/><rect x="4.5" y="5.5" width="3" height="4.5" rx="1"/><rect x="8" y="6" width="3" height="4" rx="1"/></g></svg><p>Ein bisschen Chaot und mittendrin. Ich vergesse mal ein To-do, aber nie Freunde und Familie und meine Klienten.</p></div>
      <div class="fact" style="left:110px;top:79px"><svg viewBox="0 0 12 12"><g fill="#2a3a90"><circle cx="3" cy="4" r="1.3"/><circle cx="6" cy="2.8" r="1.3"/><circle cx="9" cy="4" r="1.3"/><ellipse cx="6" cy="8.3" rx="3" ry="2.4"/></g></svg><p>Immer auf Augenhöhe. Durchaus auch bei der morgendlichen Begrüßung unserer Familienseniorin.</p></div>
      <div class="fact" style="left:187px;top:79px"><svg viewBox="0 0 12 12"><path d="M1 4 Q5 5 6 8 Q8 3 11 2 Q9 7 6 10 Q3 8 1 4Z" fill="#2a3a90"/></svg><p>Vom Langschläfer zum Early Bird. Atmung, Meditation, Dehnen, ausreichend Zeit für einen energievollen Tag – in meiner Morgenstunde schöpfe ich Energie.</p></div>
    </div>

    <div class="sec" style="top:606px;height:107px;background:var(--mid)">
      <div class="copy on-color" style="left:56px;top:18px;width:172px">
        <p>In den letzten Jahren habe ich mich in den Unternehmen, in denen ich als Personalleiter tätig war, mehr und mehr zu dem Mann für Personalprobleme und schwierige Gespräche entwickelt. Warum? Weil ich es als verstärkend empfinde, Menschen dabei zu unterstützen, ihre Potenziale zu entfalten. Weil es mein innerer Antrieb ist, zwischen Menschen zu vermitteln und alle Seiten einzubeziehen. Weil es immer eine bessere Lösung gibt und ich an Win-Win-Win-Lösungen glaube, die menschlich und wirtschaftlich sind.</p>
        <p>2022 habe ich genau das zu meinem Fokus gemacht und schließe eine Lücke für Unternehmen. Als selbstständiger Berater erarbeite ich mit Führungskräften und Mitarbeitenden Lösungen für dysfunktionale Arbeitssituationen. Beteiligend, auf Augenhöhe, wirtschaftlich.</p>
        <p style="font-weight:700">Heute sage ich: Mein Anspruch bleibt. Für jeden. Das Richtige.</p>
      </div>
    </div>

    <footer class="footer"><span>© Jonas Albrecht 2022</span><span class="links"><span>Impressum</span><span>Datenschutz</span></span></footer>
  </section>

  <section class="page page-offer" style="left:810px;top:395px;width:275px;height:757px">
    <header class="header">
      <span class="nav" style="left:28px">Start</span>
      <span class="nav is-active" style="left:63px">Angebote</span>
      <div class="brand"><span class="dot"></span><span class="name">Jonas Albrecht</span></div>
      <span class="nav" style="left:193px">Über mich</span>
      <span class="nav" style="left:230px">Kontakt</span>
    </header>
    <div class="submenu"><div class="is-active">Prozessberatung</div><div>Situationsanalyse</div><div>Coaching</div><div>Keynote Speaker</div></div>

    <div class="sec" style="top:42px;height:174px">
      <div class="photo" role="img" aria-label="Foto: Beratungsgespräch am Tisch mit Tablet" style="inset:0;background:linear-gradient(100deg,#262626 0%,#4a4440 25%,#a48866 50%,#d8c2a4 70%,#8d8f99 100%)"></div>
      <svg class="wedge" viewBox="0 0 275 174" preserveAspectRatio="none"><polygon points="0,103 140,91 275,115 275,174 0,174" fill="#8fafdc"/></svg>
      <div class="hero-claim" style="left:29px;top:34px;font-size:7.8px"><strong>GUT BERATEN</strong>So finden Sie Lösungen<br>für Ihre komplexen<br>Personalsituationen</div>
      <div class="copy on-color" style="left:54px;top:127px;width:170px">
        <p>Eine aktive Auseinandersetzung ist aufwendig und im Tagesgeschäft muss man erst mal Zeit dafür freiräumen. Als Entscheider scheuen Sie die Investition? Auch das ist verständlich. Meine Erfahrung zeigt jedoch: Dieser Weg rechnet sich schnell.</p>
        <p>Wir verändern eine Lose-Lose-Lose-Situation in eine Win-Win-Win-Situation. Weil alle Beteiligten einbezogen werden und Entwicklungschancen wieder möglich sind. Gehen wir es gemeinsam anders an.</p>
      </div>
    </div>

    <div class="sec" style="top:216px;height:294px">
      <div class="sec-title" style="top:14px;font-size:6.6px"><strong>FÜR JEDEN. DAS RICHTIGE.</strong>Ihre Prozessbegleitung mit meinem 7-Phasen-Modell</div>
      <div class="step" style="top:54px"><span class="num light">1</span><span class="txt"><strong>Bestandsaufnahme</strong>Anerkennen, was ist</span></div>
      <div class="step" style="top:79px"><span class="num navy">2</span><span class="txt"><strong>Vereinbarung</strong>Gleichberechtigt in die<br>Lösungsfindung starten</span></div>
      <div class="step" style="top:105px"><span class="num mid">3</span><span class="txt"><strong>Lösungsoptionen</strong>Mutig alle Richtungen ausloten</span></div>
      <div class="step" style="top:130px"><span class="num navy">4</span><span class="txt"><strong>Lösungsgestaltung</strong>Die zwei besten Lösungen<br>herausarbeiten</span></div>
      <div class="copy" style="left:108px;top:152px;width:96px;font-size:3px">Boost or Leave? Boost bedeutet Entwicklung, wirkliche Entwicklung. Aus der komplexen Personalsituation wird eine Entwicklungschance. Leave bedeutet das Verlassen der Situation, intern oder extern. Beides braucht das Commitment der Beteiligten. In Phase 4 arbeiten wir die beiden bestmöglichen Lösungen heraus. Es wird berücksichtigt, was für die Organisation machbar ist.</div>
      <div class="step" style="top:207px"><span class="num light">5</span><span class="txt"><strong>Entscheidung</strong>Immer eine Wahl haben</span></div>
      <div class="step" style="top:229px"><span class="num mid">6</span><span class="txt"><strong>Lösungskommunikation</strong>Im Sinne aller Beteiligten<br>umsetzen und informieren</span></div>
      <div class="step" style="top:254px"><span class="num navy">7</span><span class="txt"><strong>Check-out-Reflexion</strong>Gemeinsam reflektieren und<br>abschließen</span></div>
    </div>

    <div class="sec" style="top:510px;height:113px;background:var(--mid)">
      <div class="sec-title on-color" style="top:18px;font-size:6.4px"><strong>FÜR JEDEN. DAS RICHTIGE.</strong>Auch in der Preisgestaltung</div>
      <div class="copy on-color" style="left:54px;top:43px;width:170px">
        <p>Für jeden. Das Richtige. Das ist auch meine Haltung in der Auswahl meiner Auftraggeber. Ich möchte die Prozessberatung und -begleitung vor allem kleinen und mittelständischen Unternehmen zugänglich machen. Genauso wie sozialen Einrichtungen und Start-ups.</p>
        <p>Darüber hinaus begleite ich ebenfalls Konzerne. Mein Einsatzgebiet erstreckt sich auf den deutschsprachigen Raum. In Präsenz und digital, auf jeden Fall immer persönlich. Die Preisgestaltung erfolgt auf Augenhöhe mit Ihnen und Ihrem Unternehmen.</p>
        <p>Ich behalte mir vor, sozialen Einrichtungen andere Preise anzubieten als Wirtschaftsunternehmen. Nach einem Kennenlerngespräch und Briefing zu dem Fall erhalten Sie ein entsprechendes Angebot von mir. Eine Orientierung gibt Ihnen folgende Struktur: <strong>&gt;&gt; zur Preistabelle</strong></p>
      </div>
    </div>

    <div class="sec" style="top:623px;height:115px;background:var(--gray)">
      <div class="photo" role="img" aria-label="Foto: Berater im hellblauen Hemd, lächelnd" style="left:40px;top:22px;width:97px;height:77px;background:linear-gradient(135deg,#e7ebef,#9fb6d3 60%,#6d86ad)"></div>
      <div class="photo" role="img" aria-label="Foto: Händedruck zweier Männer im Flur" style="left:138px;top:22px;width:98px;height:77px;background:linear-gradient(90deg,#d7dbe2,#8d9ab8 45%,#efeff2 75%,#c7ccd6)"></div>
      <span class="btn" style="left:101px;top:52px">Zum Kennenlerngespräch</span>
    </div>

    <footer class="footer"><span>© Jonas Albrecht 2022</span><span class="links"><span>Impressum</span><span>Datenschutz</span></span></footer>
  </section>

</div>
</body>
</html>
```